Etiketten-Design für eingekochte Erzeugnisse
Zielgruppe
Wir sind ein regional tätiger Cateringbetrieb und Hersteller von hausgemachten, qualitativ hochwertigen Saucen, Suppen und Dips. Für unsere eingekochten Erzeugnisse suchen wir ein Etikett für durchsichtige Gläser (327 ml, TO 66) mit kupferfarbenem Twist-Off-Deep Verschluss. Da es sich um hochwertige Produkte handelt, sollte dies auch das Etikett widerspiegeln und nicht „billig“ aussehen. Das Design sollte modern, hip und farblich zum Kupferdeckel passen.
Aufgabenstellung
Das Etikett sollte über den gesamten Umfang des Glases gehen. Als Endformat stellen wir uns eine Breite des Etiketts von 220 mm und eine Höhe von 90 mm vor.
Da wir unterschiedliche Sorten anbieten, sollten sich diese in den Etiketten wiederfinden. Jede Sorte sollte also ein individuell auf den Inhalt angepasstes Etikett haben. Zudem sollte das Etikett später auch anpassbar sein, da sich die Vorschriften zur Deklaration sowie die Zutatenliste ändern können. Die Grammangabe der Gesamtmenge sollte ebenfalls anpassbar sein können.
Für unsere Marke „Topfzauber“ suchen wir außerdem ein neues Wort-Bild-Logo,
welches gleich auf dem Etikett platziert werden soll. Das Logo sollte also in das Etikett eingefügt sein, aber auch für die Homepage und den Rechnungsbogen geeignet sein.
Unser Sortiment umfasst die Saucensorten:
- Tomatensauce
- Bratensauce
- Rahmsauce
- Bolognesesauce
- Chilli con Carne
- Linsenbolognese, vegetarisch
- Gelbes Thai Curry, vegetarisch
- Ungarische Gulaschsuppe
- Karibischer Süßkartoffel-Kürbis Eintopf
- Indischer Linsencurry
Was soll auf das Etikett:
Saucen Sorte (Bezeichnung)
Hersteller:
Partyservice Hellwanger
Markus Hellwanger
Lerchenfeld 9
88999 Beispielstadt
Inhalt:
360g
Zutaten:
Anpassbares Zutatentextfeld
Anpassbare Nährwerttabelle mit den Big 7
Haltbarkeit:
Mindestens haltbar bis: siehe Deckel
Hinweise:
Kann Spuren von Sellerie und Nüssen enthalten.
Kühl, trocken und lichtgeschützt lagern.
Nach dem Öffnen im Kühlschrank aufbewahren und innerhalb weniger Tage aufbrauchen.
Weiße Fläche freihalten, um später eventuell einen Barcode einzufügen.
Internetadresse:
www.topfzauber-beispiel.de

```html
<!DOCTYPE html>
<html lang="de">
<head>
<meta charset="utf-8">
<title>Topfzauber – Etiketten</title>
<link rel="stylesheet" href="https://fonts.googleapis.com/css2?family=Montserrat:wght@300;600;800&family=Oswald:wght@300;400&display=swap">
<style>
  :root{
    --bg:#f4f2ef;
    --band:#ffffff;
    --ink:#1d1d1b;
    --tomato:#eba396;
    --mushroom:#d4a875;
    --chili:#93bfa3;
    --tomato-art-a:#f6dcd6;
    --tomato-art-b:#e7aca2;
    --mushroom-art-a:#ece2d2;
    --mushroom-art-b:#cdbb9c;
    --chili-art-a:#f4dcd8;
    --chili-art-b:#dcc1b6;
  }
  *{margin:0;padding:0;box-sizing:border-box}
  html,body{width:1200px;height:798px;overflow:hidden;background:var(--bg)}
  .canvas{position:relative;width:1200px;height:798px}
  .label{position:absolute;top:0;width:372px;height:798px}
  .label--tomato{left:16px;--accent:var(--tomato);--art-a:var(--tomato-art-a);--art-b:var(--tomato-art-b)}
  .label--mushroom{left:422px;--accent:var(--mushroom);--art-a:var(--mushroom-art-a);--art-b:var(--mushroom-art-b)}
  .label--chili{left:828px;--accent:var(--chili);--art-a:var(--chili-art-a);--art-b:var(--chili-art-b)}
  .band{position:absolute;left:0;top:347px;width:372px;height:276px;background:var(--band);box-shadow:0 1px 3px rgba(0,0,0,.08)}
  .art{position:absolute;top:372px;height:226px;background:linear-gradient(180deg,var(--art-a),var(--art-b))}
  .art--left{left:10px;width:81px}
  .art--right{right:10px;width:81px}
  .neck-strip{position:absolute;left:146px;top:131px;width:63px;height:230px;background:var(--accent)}
  .panel{position:absolute;left:101px;top:344px;width:169px;height:281px;background:var(--accent);text-align:center;color:var(--ink)}
  .brand{position:absolute;left:0;right:0;top:-30px;display:flex;align-items:center;justify-content:center;gap:6px;
    font-family:"Montserrat",sans-serif;font-weight:600;font-size:14px;color:var(--ink);letter-spacing:.5px}
  .brand-dot{width:12px;height:12px;border-radius:50%;background:var(--ink)}
  .title{margin-top:52px;font-family:"Montserrat",sans-serif;line-height:.82;font-size:44px;letter-spacing:-1.5px}
  .title b{display:block;font-weight:800}
  .title span{display:block;font-weight:300}
  .claim{margin-top:14px;font-family:"Oswald",sans-serif;font-weight:300;font-size:12.5px;line-height:18px;text-transform:uppercase;letter-spacing:.3px}
  .claim--mixed{text-transform:none;font-size:13px;line-height:21px}
  .weight{position:absolute;left:0;right:0;bottom:18px;font-family:"Oswald",sans-serif;font-weight:300;line-height:1}
  .weight small{font-size:9px;margin-right:3px}
  .weight strong{font-weight:300;font-size:27px}
  .portions{display:block;font-size:9.5px;margin-top:2px}
</style>
</head>
<body>
<main class="canvas">

  <section class="label label--tomato">
    <div class="band"></div>
    <div class="art art--left" role="img" aria-label="Aquarell-Illustration: Tomaten und Knoblauch"></div>
    <div class="art art--right" role="img" aria-label="Aquarell-Illustration: Tomaten, Knoblauch und Pfefferkörner"></div>
    <div class="neck-strip"></div>
    <div class="panel">
      <div class="brand"><i class="brand-dot"></i>Topfzauber</div>
      <h2 class="title"><b>TOM</b><b>ATEN</b><span>SAUCE</span></h2>
      <p class="claim">Vollreife aromatische<br>Tomaten und<br>mediterrane Gewürze</p>
      <p class="weight"><small>Inhalt</small><strong>360g</strong></p>
    </div>
  </section>

  <section class="label label--mushroom">
    <div class="band"></div>
    <div class="art art--left" role="img" aria-label="Zeichnung: Steinpilze mit Beeren und Kräutern"></div>
    <div class="art art--right" role="img" aria-label="Zeichnung: Steinpilze mit Schnecke und Kräutern"></div>
    <div class="neck-strip"></div>
    <div class="panel">
      <div class="brand"><i class="brand-dot"></i>Topfzauber</div>
      <h2 class="title"><b>PILZ</b><b>RAHM</b><span>SAUCE</span></h2>
      <p class="claim">Verschiedene Edelpilze<br>und frische Sahne</p>
      <p class="weight"><small>Inhalt</small><strong>360g</strong><span class="portions">Ergibt 2 Portionen</span></p>
    </div>
  </section>

  <section class="label label--chili">
    <div class="band"></div>
    <div class="art art--left" role="img" aria-label="Aquarell-Illustration: rote und grüne Chilischoten"></div>
    <div class="art art--right" role="img" aria-label="Aquarell-Illustration: rote und grüne Chilischoten"></div>
    <div class="neck-strip"></div>
    <div class="panel">
      <div class="brand"><i class="brand-dot"></i>Topfzauber</div>
      <h2 class="title"><b>CHILI</b><span>CONC</span><b>ARNE</b></h2>
      <p class="claim claim--mixed">Kidney-Beans · Rindfleisch<br>und extra scharfes Chili</p>
      <p class="weight"><small>Inhalt</small><strong>360g</strong><span class="portions">Ergibt 2 Portionen</span></p>
    </div>
  </section>

</main>
</body>
</html>
```